Criminal Defense Law Firm needs Stationary design Theme for a Business Card, Envelope, and Letterhea

Our Law Firm is seeking a general design concept for a business card, letterhead, and Envelope.

Our website is WillowcrestTrialDesk.com

A design for these three items is requested to keep branding in place for the firm. Would like to keep the Firm Colors on the website consistent with our branding on business cards, letterheads, and mailing envelopes #10 size to be exact.

We would like business cards printed front and back with Law firm Colors from website.

Letterhead with law firm colors as well. Design is not limited to just the header, but the footer can be utilized as well for email, website, phone, fax, etc.

Simple #10 envelope consisting of the same design principles set out in the previous two designs.

```html
<!DOCTYPE html>
<html lang="en">
<head>
<meta charset="utf-8">
<title>Willowcrest Trial Offices – #10 Envelope</title>
<link rel="stylesheet" href="https://fonts.googleapis.com/css2?family=Alegreya:wght@500&family=Lato:wght@300;400&display=swap">
<style>
  :root {
    --paper: #ffffff;
    --teal: #00a3b4;
    --teal-light: #7fd3dc;
    --charcoal: #262626;
    --gold: #a39266;
    --ink-light: #ffffff;
    --ink-muted: #d9d9d9;
  }
  html, body {
    margin: 0;
    padding: 0;
    width: 1200px;
    height: 781px;
    overflow: hidden;
    background: var(--paper);
  }
  .envelope {
    position: relative;
    width: 1200px;
    height: 781px;
    font-family: "Lato", Arial, sans-serif;
  }
  .envelope-flap {
    position: absolute;
    left: 0;
    top: 0;
  }
  .flap-name {
    position: absolute;
    left: 0;
    width: 1200px;
    top: 108px;
    text-align: center;
    font-family: "Alegreya", Georgia, serif;
    font-weight: 500;
    font-size: 18px;
    letter-spacing: 2px;
    text-transform: uppercase;
    color: var(--teal-light);
  }
  .envelope-body {
    position: absolute;
    left: 46px;
    top: 216px;
    width: 1109px;
    height: 521px;
    background: var(--charcoal);
  }
  .firm-band {
    position: absolute;
    left: 46px;
    top: 416px;
    width: 607px;
    height: 146px;
    background: var(--gold);
    display: flex;
    align-items: center;
  }
  .firm-mark {
    width: 64px;
    height: 64px;
    margin-left: 38px;
    border: 2.5px solid var(--ink-light);
    border-radius: 50%;
    box-sizing: border-box;
    flex: none;
  }
  .firm-name {
    margin: 0 0 0 46px;
    font-family: "Alegreya", Georgia, serif;
    font-weight: 500;
    font-size: 29px;
    line-height: 38px;
    letter-spacing: 1.2px;
    text-transform: uppercase;
    color: var(--ink-light);
  }
  .contact {
    position: absolute;
    left: 78px;
    top: 600px;
    color: var(--ink-light);
  }
  .contact-web {
    margin: 0;
    font-weight: 300;
    font-size: 37px;
    line-height: 44px;
  }
  .contact-address,
  .contact-phone {
    margin: 0;
    font-weight: 300;
    font-size: 20px;
    line-height: 25px;
    color: var(--ink-muted);
  }
  .contact-phone {
    display: flex;
    align-items: center;
    gap: 8px;
  }
  .phone-icon {
    width: 18px;
    height: 18px;
    flex: none;
  }
</style>
</head>
<body>
  <main class="envelope">
    <svg class="envelope-flap" width="1200" height="230" viewBox="0 0 1200 230" aria-hidden="true">
      <path d="M46 216 L46 192 L118 58 Q136 25 180 25 L1022 25 Q1066 25 1084 58 L1155 192 L1155 216 Z" fill="var(--teal)"/>
    </svg>
    <div class="flap-name">Willowcrest</div>

    <div class="envelope-body"></div>

    <div class="firm-band">
      <span class="firm-mark" aria-hidden="true"></span>
      <h1 class="firm-name">Willowcrest Trial<br>Offices</h1>
    </div>

    <address class="contact" style="font-style: normal;">
      <p class="contact-web">www.willowcresttrialdesk.com</p>
      <p class="contact-address">2140 Larkspur Avenue, Fairhaven, NM 87000</p>
      <p class="contact-phone">
        <svg class="phone-icon" viewBox="0 0 18 18" aria-hidden="true">
          <circle cx="9" cy="9" r="9" fill="var(--ink-light)"/>
          <path d="M6.2 4.6 L7.6 6.6 L6.8 7.6 Q7.6 9.6 10.2 11 L11.2 10.2 L13.2 11.6 L12.4 13.2 Q8.8 13.4 6.2 10.6 Q4.4 8.2 4.8 5.6 Z" fill="var(--charcoal)"/>
        </svg>
        555.014.2290
      </p>
    </address>
  </main>
</body>
</html>
```